Business Card and Letterhead for Vantel Psychology

We need a business card design and letterhead to use for our Psychology firm that specializes in psychoeducational assessments and individual therapy. Our motto is Purpose-Driven Assessments, Meaning-Centered Therapy.Our contact information is as follows:
Vantel Psychology
The Bramwick Block - 4127-38St.
Box 6154 Olds, AB
T2K 3R8
t 403.555.0148 (VANT)
f 403.555.0193
www.vantelpsych-example.ca
The business card will be used for two different psychologists so I can supply names nearer to completion. We prefer clean, uncluttered looks.

Target Market(s)

Clients, Educators

Font styles to use
Sans Serif

Colors

Designer to choose colors to be used in the design.

Requirements
Must have
• All relevant contact info, logo, some "white" space.
Nice to have
• It would be nice to see letterhead options that have the logo on the top of the page but also options that have it on the side. I think top of the page is probably our preference.
Should not have
• Too much clutter!

```html
<!DOCTYPE html>
<html lang="en">
<head>
<meta charset="utf-8">
<title>Vantel Psychology – Business Card</title>
<link rel="stylesheet" href="https://fonts.googleapis.com/css2?family=Open+Sans:wght@400;600;700&display=swap">
<style>
  :root {
    --backdrop: #d9d8d4;
    --paper: #f7f7f5;
    --brand-blue: #4fb1d3;
    --brand-orange: #f08a2c;
    --ink: #5a5a5a;
    --ink-soft: #7a7a7a;
    --card-shadow: rgba(0, 0, 0, 0.18);
  }
  * { box-sizing: border-box; margin: 0; padding: 0; }
  html, body {
    width: 1200px;
    height: 857px;
    overflow: hidden;
    background: var(--backdrop);
    font-family: "Open Sans", Arial, sans-serif;
  }
  .card-set {
    width: 1200px;
    height: 857px;
    display: flex;
    align-items: center;
    justify-content: center;
    gap: 60px;
  }
  .card {
    position: relative;
    width: 525px;
    height: 300px;
    background: var(--paper);
    border-bottom: 4px solid var(--brand-orange);
    box-shadow: 0 10px 26px var(--card-shadow);
  }

  /* Front face */
  .card-front .identity {
    position: absolute;
    left: 40px;
    top: 44px;
  }
  .identity .person-name {
    font-size: 17px;
    font-weight: 700;
    letter-spacing: 0.5px;
    color: var(--brand-blue);
    text-transform: uppercase;
  }
  .identity .person-role {
    font-size: 11.5px;
    color: var(--ink-soft);
    margin-top: 2px;
  }
  .identity .accent-rule {
    width: 40px;
    height: 2px;
    background: var(--brand-orange);
    margin-top: 9px;
  }
  .card-front .address {
    position: absolute;
    left: 40px;
    top: 140px;
    font-size: 11px;
    line-height: 1.5;
    color: var(--ink);
  }
  .card-front .contact-list {
    position: absolute;
    left: 40px;
    top: 186px;
    list-style: none;
    font-size: 11px;
    line-height: 1.5;
    color: var(--ink);
  }
  .contact-list li {
    display: flex;
    align-items: center;
    gap: 8px;
  }
  .contact-list svg {
    width: 10px;
    height: 10px;
    flex: none;
  }
  .card-front .brand-mark {
    position: absolute;
    right: 44px;
    top: 70px;
    width: 170px;
    display: flex;
    flex-direction: column;
    align-items: center;
    gap: 14px;
  }
  .brand-mark .brand-dot {
    width: 110px;
    height: 110px;
    border-radius: 50%;
    background: var(--brand-blue);
  }
  .brand-mark .brand-name {
    font-size: 15px;
    font-weight: 600;
    color: var(--brand-blue);
    letter-spacing: 0.5px;
  }

  /* Back face */
  .card-back {
    display: flex;
    flex-direction: column;
    align-items: center;
    justify-content: center;
    gap: 16px;
  }
  .card-back .brand-dot {
    width: 70px;
    height: 70px;
    border-radius: 50%;
    background: var(--brand-blue);
  }
  .card-back .brand-name {
    font-size: 26px;
    font-weight: 600;
    letter-spacing: 1.5px;
    color: var(--brand-orange);
    text-transform: uppercase;
  }
</style>
</head>
<body>
  <main class="card-set">
    <section class="card card-front" aria-label="Business card front">
      <div class="identity">
        <p class="person-name">Marlo T. Quenby</p>
        <p class="person-role">Operational Manager</p>
        <div class="accent-rule"></div>
      </div>

      <p class="address">
        The Bramwick Block - 4127-38St.<br>
        Box 6154 Olds, AB | T2K 3R8
      </p>

      <ul class="contact-list">
        <li>
          <svg viewBox="0 0 10 10" aria-hidden="true"><path d="M2 1 L4 1 L4.6 3 L3.4 3.8 Q4.2 5.6 6.2 6.6 L7 5.4 L9 6 L9 8 Q5 9.4 1.6 5 Q0.6 3 2 1Z" fill="var(--brand-orange)"/></svg>
          403.555.0148 (VANT)
        </li>
        <li>
          <svg viewBox="0 0 10 10" aria-hidden="true"><rect x="2.5" y="0.5" width="5" height="3" fill="var(--brand-orange)"/><rect x="0.5" y="3.5" width="9" height="4" rx="1" fill="var(--brand-orange)"/><rect x="2.5" y="6.5" width="5" height="3" fill="var(--brand-orange)"/></svg>
          403.555.0193
        </li>
        <li>
          <svg viewBox="0 0 10 10" aria-hidden="true"><rect x="0.5" y="2" width="9" height="6" rx="1" fill="var(--brand-orange)"/><path d="M1 2.5 L5 5.5 L9 2.5" stroke="var(--paper)" stroke-width="1" fill="none"/></svg>
          info@vantelpsych-example.ca
        </li>
        <li>
          <svg viewBox="0 0 10 10" aria-hidden="true"><circle cx="5" cy="5" r="4.3" fill="var(--brand-orange)"/><path d="M0.8 5 H9.2 M5 0.8 Q2.6 5 5 9.2 M5 0.8 Q7.4 5 5 9.2" stroke="var(--paper)" stroke-width="0.7" fill="none"/></svg>
          www.vantelpsych-example.ca
        </li>
      </ul>

      <div class="brand-mark">
        <div class="brand-dot"></div>
        <p class="brand-name">Vantel Psychology</p>
      </div>
    </section>

    <section class="card card-back" aria-label="Business card back">
      <div class="brand-dot"></div>
      <p class="brand-name">Vantel Psychology</p>
    </section>
  </main>
</body>
</html>
```